A Recruitment Company Needs a Web Design that Expresses High Energy and Results

Our company, BrightLane Consultants, needs a web design for our recruiting business based in Asia (Taiwan). We provide recruitment services to many international companies. Our client base is as follows:
Hi-Tech - 60%
Healthcare and Consumer/FMCG - 15%
Industrial and Engineering - 15%
Banking and Finance - 10%

The website will be accessed by both clients and job seekers. As such, it should look professional, user-friendly and is interactive.

Sans Serif

add136
ffffff
000000

• Attached is the company's logo. the design mus be in line with it.

```html
<!DOCTYPE html>
<html lang="en">
<head>
<meta charset="utf-8">
<title>BrightLane Consultants</title>
<link rel="stylesheet" href="https://fonts.googleapis.com/css2?family=Open+Sans:ital,wght@0,300;0,400;0,600;0,700;1,400&display=swap">
<style>
:root{
  --green:#add136;
  --green-dark:#2e7d1f;
  --ink:#3d3d3d;
  --muted:#8a8a8a;
  --dark:#262626;
  --darker:#1d1d1d;
  --white:#ffffff;
  --track:#d9d9d9;
}
*{margin:0;padding:0;box-sizing:border-box}
html,body{width:1200px;height:2387px;overflow:hidden}
body{font-family:"Open Sans",Arial,sans-serif;color:var(--ink);background:var(--white);position:relative}
a{color:inherit;text-decoration:none}

/* header */
.site-header{position:absolute;left:0;top:0;width:1200px;height:72px;background:var(--white);border-bottom:1px solid #e6e6e6}
.brand{position:absolute;left:99px;top:22px;font-size:20px;font-weight:700;color:var(--green);letter-spacing:-.2px}
.main-nav a{position:absolute;top:29px;font-size:11px;color:#555;transform:translateX(-50%);white-space:nowrap}

/* hero */
.hero{position:absolute;left:0;top:72px;width:1200px;height:480px}
.hero-photo{position:absolute;inset:0;background:linear-gradient(90deg,#3c4656 0%,#6f6d6c 28%,#c9c4b8 48%,#f4f1e4 62%,#fbf9ef 100%)}
.hero-copy{position:absolute;left:630px;top:130px}
.hero-copy .l1{font-size:30px;font-weight:700;color:#1e1e1e;line-height:36px}
.hero-copy .l2{font-size:38px;font-weight:700;color:var(--green);line-height:44px}
.hero-copy .l3{font-size:27px;font-weight:300;color:#2a2a2a;line-height:36px;letter-spacing:.3px}
.btn-green{position:absolute;left:633px;top:264px;width:218px;height:48px;background:var(--green);color:var(--white);font-size:11px;display:flex;align-items:center;justify-content:center}
.hero-arrow{position:absolute;top:203px;width:32px;height:32px;border-radius:50%;background:rgba(255,255,255,.45);display:flex;align-items:center;justify-content:center}

/* welcome */
.welcome{position:absolute;left:0;top:552px;width:1200px;height:285px;background:var(--dark)}
.welcome-title{position:absolute;right:699px;top:80px;text-align:right}
.welcome-title .small{font-size:32px;font-weight:300;color:#9a9a9a;line-height:40px}
.welcome-title .big{font-size:54px;font-weight:700;color:var(--green);line-height:62px}
.welcome-text{position:absolute;left:597px;top:56px;width:432px;font-family:Arial,sans-serif;font-size:10.5px;line-height:21px;color:var(--white)}
.welcome-text p+p{margin-top:13px}

/* services */
.services{position:absolute;left:0;top:837px;width:1200px;height:484px}
.section-title{position:absolute;left:0;width:1200px;text-align:center;font-size:29px;font-weight:700;color:#444}
.section-sub{position:absolute;left:0;width:1200px;text-align:center;font-size:15px;color:#8a8a8a}
.service{position:absolute;top:185px;width:240px;transform:translateX(-50%);text-align:center}
.service-icon{width:86px;height:86px;border-radius:50%;background:#3f3f3f;margin:0 auto;display:flex;align-items:center;justify-content:center}
.service-icon.active{background:var(--green)}
.service h3{margin-top:18px;font-size:14px;font-weight:700;color:#333;line-height:22px}
.service p{width:186px;margin:10px auto 0;font-size:11.5px;color:#8a8a8a;line-height:20px}

/* about */
.about{position:absolute;left:0;top:1321px;width:1200px;height:433px}
.about-photo{position:absolute;inset:0;background:linear-gradient(90deg,#1f1f1f 0%,#3b3b3b 30%,#2a2a2a 55%,#4a4a4a 80%,#2b2b2b 100%)}
.about-title{position:absolute;top:105px;left:0;width:1200px;text-align:center;font-size:29px;font-weight:700;color:var(--white)}
.about-sub{position:absolute;top:155px;left:0;width:1200px;text-align:center;font-size:20px;font-weight:300;color:var(--white)}
.about-text{position:absolute;top:200px;left:200px;width:800px;text-align:center;font-family:Arial,sans-serif;font-size:14px;line-height:29px;color:var(--white)}
.btn-outline{position:absolute;left:500px;top:288px;width:202px;height:46px;border:2px solid var(--white);color:var(--white);font-size:11px;display:flex;align-items:center;justify-content:center}

/* testimonials & client base */
.block-title{position:absolute;top:1822px;font-size:17px;font-weight:700;color:#222}
.slider-arrows{position:absolute;left:614px;top:1826px;font-size:13px;color:#aaa;letter-spacing:6px}
.avatar{position:absolute;left:100px;top:1880px;width:116px;height:116px;border-radius:50%;background:radial-gradient(circle at 50% 40%,#7a7a7a,#2f2f2f)}
.quote{position:absolute;left:270px;top:1886px;width:380px;font-family:Arial,sans-serif;font-size:11.5px;font-style:italic;color:#999;line-height:23px}
.quote-mark{position:absolute;font-size:34px;color:#cfcfcf;font-family:Georgia,serif;line-height:1}
.client-name{position:absolute;left:270px;top:1980px;font-size:11px;font-weight:700;color:var(--green-dark)}
.client-role{position:absolute;left:270px;top:2001px;font-size:12px;color:#999}
.bar{position:absolute;left:707px;width:372px;height:20px;background:var(--track);font-size:10px;font-weight:700;color:#333}
.bar .fill{position:absolute;left:0;top:0;height:20px;background:var(--green);color:var(--white);padding-left:15px;line-height:20px}
.bar .label{position:absolute;right:12px;top:0;line-height:20px}

/* footer */
.site-footer{position:absolute;left:0;top:2090px;width:1200px;height:246px;background:var(--dark)}
.footer-col{position:absolute;top:40px}
.footer-col h4{font-size:12px;font-weight:700;color:#cfcfcf;letter-spacing:.3px}
.footer-col p{margin-top:18px;font-family:Arial,sans-serif;font-size:10.5px;line-height:23px;color:#c7c7c7}
.footer-col ul{list-style:none;margin-top:14px}
.footer-col li{font-family:Arial,sans-serif;font-size:10.5px;line-height:22px;color:#c7c7c7}
.social li{display:flex;align-items:center;height:35px;line-height:35px;color:#8a8a8a}
.social .sq{width:24px;height:24px;border:1px solid #5a5a5a;background:#333;margin-right:16px}
.copyright{position:absolute;left:0;top:2336px;width:1200px;height:51px;background:var(--darker);text-align:center;line-height:51px;font-size:10.5px;color:#8a8a8a}
</style>
</head>
<body>

<header class="site-header">
  <div class="brand">BrightLane Consultants</div>
  <nav class="main-nav">
    <a style="left:503px">HOME</a>
    <a style="left:602px">ABOUT US</a>
    <a style="left:713px">SERVICES</a>
    <a style="left:820px">CAREERS</a>
    <a style="left:939px">TESTIMONIALS</a>
    <a style="left:1066px">CONTACT US</a>
  </nav>
</header>

<section class="hero">
  <div class="hero-photo" role="img" aria-label="Photo of smiling business professionals seated in a row at a bright office interview"></div>
  <div class="hero-copy">
    <div class="l1">WE PROVIDE</div>
    <div class="l2">RECRUITMENT SERVICES</div>
    <div class="l3">TO MANY INTERNATIONAL COMPANIES</div>
  </div>
  <a class="btn-green">CLICK HERE FOR VIEW DETAILS</a>
  <div class="hero-arrow" style="left:35px"><svg width="12" height="14" viewBox="0 0 12 14"><path d="M9 1 3 7l6 6" fill="none" stroke="#fff" stroke-width="2.5"/></svg></div>
  <div class="hero-arrow" style="left:1141px"><svg width="12" height="14" viewBox="0 0 12 14"><path d="M3 1l6 6-6 6" fill="none" stroke="#fff" stroke-width="2.5"/></svg></div>
</section>

<section class="welcome">
  <div class="welcome-title">
    <div class="small">WELCOME TO</div>
    <div class="big">BRIGHTLANE</div>
  </div>
  <div class="welcome-text">
    <p>Lorem Ipsum is simply dummy text of the printing and typesetting industry. Lorem Ipsum has been the industry's standard dummy text ever since the 1500s, when an unknown printer took a galley of type and scrambled it to make a type specimen book. It has survived not only five centuries, but also the leap into electronic typesetting, remaining essentially unchanged.</p>
    <p>It was popularised in the 1960s with the release of Lumatype sheets containing Lorem Ipsum passages, and more recently with desktop publishing software like Pagecraft Studio including versions of Lorem Ipsum.</p>
  </div>
</section>

<section class="services">
  <h2 class="section-title" style="top:68px">OUR SERVICES</h2>
  <div class="section-sub" style="top:116px">Es simplemente el texto de relleno de las imprentas y archivos gende texto ha sido...</div>

  <div class="service" style="left:199px">
    <div class="service-icon active"><svg width="36" height="30" viewBox="0 0 36 30"><path d="M2 2v26h32" fill="none" stroke="#fff" stroke-width="2.5"/><rect x="8" y="16" width="4" height="9" fill="#fff"/><rect x="15" y="10" width="4" height="15" fill="#fff"/><rect x="22" y="13" width="4" height="12" fill="#fff"/><rect x="29" y="7" width="4" height="18" fill="#fff"/></svg></div>
    <h3>ES SIMPLEMENTE E<br>TEXTO DE RELLENO DE LAS</h3>
    <p>Es simplemente el texto de relleno de las imprentas y archivos gende texto ha sido...</p>
  </div>
  <div class="service" style="left:466px">
    <div class="service-icon"><svg width="36" height="32" viewBox="0 0 36 32"><rect x="2" y="2" width="32" height="21" rx="2" fill="#fff"/><rect x="5" y="5" width="26" height="15" fill="#3f3f3f"/><rect x="15" y="23" width="6" height="5" fill="#fff"/><rect x="10" y="28" width="16" height="3" fill="#fff"/></svg></div>
    <h3>ES SIMPLEMENTE E<br>TEXTO DE RELLENO DE LAS</h3>
    <p>Es simplemente el texto de relleno de las imprentas y archivos gende texto ha sido...</p>
  </div>
  <div class="service" style="left:737px">
    <div class="service-icon"><svg width="40" height="30" viewBox="0 0 40 30"><circle cx="9" cy="9" r="4" fill="#fff"/><circle cx="31" cy="9" r="4" fill="#fff"/><circle cx="20" cy="8" r="5.5" fill="#fff"/><path d="M2 24c0-6 3-9 7-9s6 2 6 4v5z" fill="#fff"/><path d="M38 24c0-6-3-9-7-9s-6 2-6 4v5z" fill="#fff"/><path d="M11 28c0-8 4-12 9-12s9 4 9 12z" fill="#fff"/></svg></div>
    <h3>ES SIMPLEMENTE E<br>TEXTO DE RELLENO DE LAS</h3>
    <p>Es simplemente el texto de relleno de las imprentas y archivos gende texto ha sido...</p>
  </div>
  <div class="service" style="left:1001px">
    <div class="service-icon"><svg width="38" height="34" viewBox="0 0 38 34"><circle cx="14" cy="20" r="9" fill="none" stroke="#fff" stroke-width="5" stroke-dasharray="4 3"/><circle cx="14" cy="20" r="3" fill="#fff"/><circle cx="29" cy="9" r="6" fill="none" stroke="#fff" stroke-width="4" stroke-dasharray="3 2.3"/><circle cx="29" cy="9" r="2" fill="#fff"/></svg></div>
    <h3>ES SIMPLEMENTE E<br>TEXTO DE RELLENO DE LAS</h3>
    <p>Es simplemente el texto de relleno de las imprentas y archivos gende texto ha sido...</p>
  </div>
</section>

<section class="about">
  <div class="about-photo" role="img" aria-label="Black and white photo of business people shaking hands at a meeting"></div>
  <h2 class="about-title">ABOUT BRIGHTLANE</h2>
  <div class="about-sub">ES SIMPLEMENTE EL TEXTO DE RELLENO DE LAS IMPRENTAS Y ARCHIVOS DE</div>
  <p class="about-text">It is a long established fact that a reader will be distracted by the readable content of a page when looking at its layout. The point of using Lorem Ipsum is that it has a more-or-less normal distribution of letters...</p>
  <a class="btn-outline">CLICK HERE FOR MORE INFO</a>
</section>

<section class="testimonials">
  <h3 class="block-title" style="left:99px">WHAT OUR CLIENTS SAY</h3>
  <div class="slider-arrows">‹ ›</div>
  <div class="avatar" role="img" aria-label="Round portrait photo of the client giving the testimonial"></div>
  <span class="quote-mark" style="left:244px;top:1876px">“</span>
  <p class="quote">Lorem Ipsum is simply dummy text of the printing and typesetting industry. Lorem Ipsum has been the industry's standard dummy text ever since the 1500s, when an unknown printer took a galley...</p>
  <span class="quote-mark" style="left:630px;top:1940px">”</span>
  <div class="client-name">MARCUS HALE</div>
  <div class="client-role">Business man</div>
</section>

<section class="client-base">
  <h3 class="block-title" style="left:708px">OUR CLIENT BASE IS AS FOLLOWS</h3>
  <div class="bar" style="top:1874px"><div class="fill" style="width:78px">6%</div><span class="label">HI-TECH</span></div>
  <div class="bar" style="top:1909px"><div class="fill" style="width:142px">15%</div><span class="label">HEALTHCARE AND CONSUMER/FMCG</span></div>
  <div class="bar" style="top:1943px"><div class="fill" style="width:142px">15%</div><span class="label">INDUSTRIAL AND ENGINEERING</span></div>
  <div class="bar" style="top:1978px"><div class="fill" style="width:142px">15%</div><span class="label">BANKING AND FINANCE</span></div>
</section>

<footer class="site-footer">
  <div class="footer-col" style="left:119px;width:310px">
    <h4>WHAT WE DO ?</h4>
    <p>Es simplemente el texto de relleno de las imprentas y archivos de texto. Lorem Ipsum ha sido el texto de relleno estándar de las industrias desde el año 1500, cuando un impresor ha sido el texto de relleno estándar de las industrias desde el año 1500, cuando un impresor...</p>
  </div>
  <div class="footer-col" style="left:532px">
    <h4>WELCOME</h4>
    <ul><li>Home</li><li>About Us</li><li>Services</li><li>Careers</li><li>Testimonials</li><li>Contact Us</li></ul>
  </div>
  <div class="footer-col" style="left:720px">
    <h4>INFORMATION</h4>
    <ul><li>Terms &amp; Conditions</li><li>Privacy Policy</li><li>Disclaimer</li><li>Sitemap</li></ul>
  </div>
  <div class="footer-col social" style="left:937px">
    <h4>FOLLOW US</h4>
    <ul>
      <li><span class="sq"></span>Socialpage</li>
      <li><span class="sq"></span>Chirper</li>
      <li><span class="sq"></span>Circlenet</li>
      <li><span class="sq"></span>Worklink</li>
    </ul>
  </div>
</footer>
<div class="copyright">© Copyrights. 2015. BrightLane. All rights reserved.</div>

</body>
</html>
```